Harbor Oak Works business cards

I’d like a business card design that includes my logo, a tag line and my contact info. Black, textured background. My contact info color should match the orange and blue gradients. Tagline under logo: “Wooden Tables and Furniture of the Highest Quality”

Target Market(s)

High end furniture buyers

Contact Information for Business Card

Contact info, logo and tagline

```html
<!DOCTYPE html>
<html lang="en">
<head>
<meta charset="utf-8">
<title>Harbor Oak Works – Business Cards</title>
<link rel="stylesheet" href="https://fonts.googleapis.com/css2?family=Montserrat:wght@400;500;700&family=Poppins:wght@600&display=swap">
<style>
  :root {
    --page-bg: #2a2a2a;
    --card-black: #0c0c0c;
    --card-edge: #1c1c1c;
    --brand-orange: #ef7a21;
    --brand-blue: #1f63b3;
    --text-light: #d9d9d9;
    --text-silver: #c4c4c4;
    --rule-grey: #777777;
  }
  * { margin: 0; padding: 0; box-sizing: border-box; }
  html, body {
    width: 1200px; height: 900px; overflow: hidden;
    background: var(--page-bg);
  }
  .sheet {
    width: 1200px; height: 900px;
    display: flex; align-items: center; justify-content: center; gap: 60px;
  }
  .card {
    position: relative;
    width: 525px; height: 300px;
    border-radius: 18px;
    background:
      radial-gradient(circle at 30% 30%, rgba(255,255,255,0.04), transparent 60%),
      var(--card-black);
    box-shadow: 0 0 0 1px var(--card-edge);
    overflow: hidden;
  }

  /* Front: contact side */
  .front-brand {
    position: absolute; left: 30px; top: 168px;
    width: 215px;
  }
  .front-brand-row {
    display: flex; align-items: center; gap: 8px;
  }
  .brand-dot {
    width: 12px; height: 12px; border-radius: 50%; flex: none;
    background: var(--brand-orange);
  }
  .brand-name {
    font-family: "Montserrat", sans-serif; font-weight: 500;
    white-space: nowrap;
  }
  .front-brand .brand-name {
    font-size: 20px; color: var(--brand-blue);
  }
  .front-rule {
    width: 130px; height: 1px; background: var(--brand-orange);
    margin: 6px 0 0 60px;
  }
  .divider {
    position: absolute; left: 262px; top: 70px;
    width: 1.5px; height: 190px; background: var(--brand-blue);
  }
  .contact {
    position: absolute; left: 284px; top: 60px;
    font-family: "Montserrat", sans-serif; color: var(--text-light);
  }
  .contact-name {
    font-weight: 700; font-size: 17px; color: var(--brand-orange);
    letter-spacing: 0.5px; text-transform: uppercase; line-height: 20px;
  }
  .contact-role { font-size: 13px; margin-bottom: 12px; }
  .contact-list { list-style: none; }
  .contact-list li {
    display: flex; align-items: center; gap: 8px;
    font-size: 13px; line-height: 21px;
  }
  .contact-list svg { width: 12px; height: 12px; flex: none; }
  .address { font-size: 13px; line-height: 18px; margin-top: 12px; }

  /* Back: brand side */
  .card-back {
    display: flex; flex-direction: column; align-items: center; justify-content: center;
  }
  .back-brand {
    display: flex; align-items: center; gap: 14px;
  }
  .back-brand .brand-dot { width: 20px; height: 20px; background: var(--text-silver); }
  .back-brand .brand-name { font-size: 34px; color: var(--text-silver); }
  .back-rule {
    width: 210px; height: 1px; background: var(--rule-grey); margin: 10px 0 18px 120px;
  }
  .tagline {
    font-family: "Poppins", sans-serif; font-weight: 600;
    font-size: 14px; color: var(--text-silver);
  }
</style>
</head>
<body>
<main class="sheet">
  <section class="card card-front" aria-label="Business card, contact side">
    <div class="front-brand">
      <div class="front-brand-row">
        <span class="brand-dot"></span>
        <span class="brand-name">Harbor Oak Works</span>
      </div>
      <div class="front-rule"></div>
    </div>
    <div class="divider"></div>
    <div class="contact">
      <p class="contact-name">Daniel Reyes</p>
      <p class="contact-role">Managing Director</p>
      <ul class="contact-list">
        <li>
          <svg viewBox="0 0 24 24" aria-hidden="true"><path fill="var(--brand-orange)" d="M6.6 10.8a15 15 0 0 0 6.6 6.6l2.2-2.2a1 1 0 0 1 1-.25 11.4 11.4 0 0 0 3.6.57 1 1 0 0 1 1 1V20a1 1 0 0 1-1 1A17 17 0 0 1 3 4a1 1 0 0 1 1-1h3.5a1 1 0 0 1 1 1c0 1.250.2 2.45.57 3.57a1 1 0 0 1-.25 1z"/></svg>
          044-555 019 284
        </li>
        <li>
          <svg viewBox="0 0 24 24" aria-hidden="true"><rect x="2" y="5" width="20" height="14" rx="1" fill="var(--brand-orange)"/><path d="M2 6l10 7 10-7" fill="none" stroke="var(--card-black)" stroke-width="1.6"/></svg>
          hello@harboroakworks.com
        </li>
        <li>
          <svg viewBox="0 0 24 24" aria-hidden="true"><g fill="none" stroke="var(--brand-orange)" stroke-width="2"><circle cx="12" cy="12" r="9"/><ellipse cx="12" cy="12" rx="4" ry="9"/><path d="M3 12h18M5 7h14M5 17h14"/></g></svg>
          www.harboroakworks.com
        </li>
      </ul>
      <p class="address">421, Address line goes here<br>45452,Country Name</p>
    </div>
  </section>

  <section class="card card-back" aria-label="Business card, brand side">
    <div class="back-brand">
      <span class="brand-dot"></span>
      <span class="brand-name">Harbor Oak Works</span>
    </div>
    <div class="back-rule"></div>
    <p class="tagline">Wooden Tables and Furniture of the Highest Quality</p>
  </section>
</main>
</body>
</html>
```